Marketplace Web Re-design overhaul @corvahub

Hi,
We are currently in production with a website that is getting some mixed feedback about visual appeal and usability. We are using a responsive design and need to stay true to the logo colours and other marketing collateral we have in place. I will provide a brochure with the colour palate we use for some guidance. If you can please help us design something fresh and modern to communicate the essence of our company. The brochure will be a good summary of what we do and who we are targeting as customers. Our current website can be found at www.corvahub.com. If there is any questions, please let me know.

Target Market(s)

Contractors and Corporate Companies

Industry/Entity Type

Information Technology

Number of Pages Required

4 page

Requirements
Must have
• Must have a complete new visual look, including
• 1. Images
• 2. Background colour scheme overhaul (not black)
• 3. re-design of the layout but keep to similar page breakdowns
Nice to have
• Some of the pages are a bit wordy, happy to have suggestions on how to reduce.
• Would be great if we can integrate the Drift.ON! blog page to the Corvahub page?
• This is some feedback a fellow UX designer provided to improve our CRO
• First off when you land on the home page, who is your audience? Are you everything to everyone? Even after watching the video (https://www.vidplex-example.com/watch?v=q-RtnB7LpX3), I do not know what markets you service or who this app will be for.
• Your main headline and paragraph above the fold I find unnecessarily wordy and an overuse of 'buzzwords' . Perhaps you could look at appealing to the lowest common denominator and make it very simple and put it all into a simple sentence.
• The main hero image to the right of the headline offers no emotional pull at all. I'm assuming it's just a screenshot of your dashboard? Personally, I would be looking at using a person's image in that space.
• Also in this space, increase the size of your 'register' button. On the topic of your register button, you have it in different colours. Green in header, and red in content. Make it the same colour, and don't use that colour again on the site. That colour is to become your call to action (CTA) colour. Understandably you'll have three different colours for the account type, and again, don't use these colours anywhere else on the site.
• The registration area where the three account types are where you choose which one suits you, it's extremely busy with background images and heavy use of text. If you were my client, I would be advising you to ditch the bg image (including the iPad shot), keeping the text, making the register icons much bigger. Perhaps instead of bg images, use a solid colour for each (green, orange, red). I'm highly confident this change will make a massive difference in your sign up rate.
Should not have
• Please keep to the fonts used on the original website
• Keep to the colour provided on the company brochure for guidance.

```html
<!DOCTYPE html>
<html lang="en">
<head>
<meta charset="utf-8">
<title>Corvahub — Our Partners</title>
<link href="https://fonts.googleapis.com/css2?family=Arimo:wght@400;500&display=swap" rel="stylesheet">
<style>
  :root {
    --green: #3fb34f;
    --green-footer: #43a94d;
    --green-bar: #379240;
    --section-bg: #e8ebef;
    --ink: #2f3336;
    --body-ink: #4a4f55;
    --white: #ffffff;
    --rule: #b9bec4;
    --brand-red: #d63a3a;
    --hero-top: #8d8f94;
    --hero-mid: #6e6a6c;
    --hero-bottom: #3b3a3d;
  }
  * { margin: 0; padding: 0; box-sizing: border-box; }
  html, body { width: 952px; height: 1200px; overflow: hidden; }
  body { position: relative; font-family: "Arimo", Arial, sans-serif; color: var(--ink); background: var(--section-bg); }

  .hero {
    position: absolute; left: 0; top: 0; width: 952px; height: 519px;
    background:
      radial-gradient(ellipse 300px 180px at 330px 360px, rgba(40,36,38,.55), transparent),
      linear-gradient(90deg, #b9b9bd 0%, var(--hero-top) 18%, #9c8a84 55%, var(--hero-mid) 80%, var(--hero-bottom) 100%);
  }
  .hero-shade { position: absolute; inset: 0; background: linear-gradient(180deg, rgba(0,0,0,.05) 0%, rgba(0,0,0,.1) 60%, rgba(0,0,0,.25) 100%); }
  .hero-text {
    position: absolute; left: 226px; top: 226px; width: 500px;
    text-align: center; color: var(--white); font-size: 14.4px; line-height: 17.4px;
  }

  .site-nav { position: absolute; left: 0; top: 0; width: 952px; height: 38px; border-bottom: 1px solid rgba(255,255,255,.25); }
  .brand { position: absolute; display: flex; align-items: center; gap: 5px; font-size: 14px; color: var(--white); letter-spacing: .5px; }
  .brand-dot { width: 12px; height: 12px; border-radius: 50%; background: var(--green); }
  .site-nav .brand { left: 126px; top: 11px; }
  .nav-link { position: absolute; top: 14px; font-size: 8.8px; color: var(--white); text-decoration: none; }
  .nav-link.is-active::after { content: ""; position: absolute; left: -1px; right: -1px; top: 21px; height: 2px; background: var(--green); }
  .account-link { position: absolute; top: 14px; font-size: 7.2px; color: var(--white); }
  .account-link.register { color: var(--green); }

  .section-title { position: absolute; left: 0; width: 952px; top: 548px; text-align: center; font-size: 19px; font-weight: 500; letter-spacing: 1.4px; color: var(--ink); }
  .title-rule { position: absolute; left: 423px; top: 580px; width: 103px; height: 3px; background: var(--green); }

  .partner-mark { position: absolute; display: flex; align-items: center; gap: 6px; font-size: 17px; font-weight: 500; color: var(--ink); }
  .mark-square { width: 16px; height: 16px; background: var(--ink); }
  .badge-shape { position: absolute; border: 3px solid var(--green); border-radius: 3px; }

  .partner-name { position: absolute; font-size: 12.2px; color: var(--green); }
  .partner-rule { position: absolute; height: 1px; background: var(--rule); }
  .partner-copy { position: absolute; font-size: 7.6px; line-height: 10px; color: var(--body-ink); }

  .site-footer { position: absolute; left: 0; top: 1000px; width: 952px; height: 168px; background: var(--green-footer); color: var(--white); }
  .site-footer .brand { left: 164px; top: 39px; font-size: 13px; }
  .footer-about { position: absolute; left: 164px; top: 70px; width: 160px; font-size: 7.8px; line-height: 10px; }
  .footer-heading { position: absolute; top: 38px; font-size: 9.6px; letter-spacing: .3px; }
  .footer-rule { position: absolute; top: 50px; height: 1px; background: rgba(255,255,255,.5); }
  .footer-links { position: absolute; top: 66px; list-style: none; font-size: 8px; line-height: 14.4px; }
  .newsletter-note { position: absolute; left: 626px; top: 67px; font-size: 8px; }
  .newsletter-field { position: absolute; left: 626px; top: 1094px; }
  .email-field { position: absolute; left: 626px; top: 94px; width: 161px; height: 20px; border: 1px solid var(--white); font-size: 8.4px; padding: 5px 9px; }
  .email-arrow { position: absolute; right: 8px; top: 6px; }

  .legal-bar { position: absolute; left: 0; top: 1168px; width: 952px; height: 32px; background: var(--green-bar); color: var(--white); }
  .copyright { position: absolute; left: 164px; top: 12px; font-size: 7px; }
  .social-links { position: absolute; left: 734px; top: 12px; display: flex; gap: 8px; }
  .social-dot { width: 8px; height: 8px; border-radius: 50%; background: var(--white); }
</style>
</head>
<body>

<header class="hero">
  <div class="hero-shade" role="img" aria-label="Blurred photo of hands typing on a laptop keyboard at a desk"></div>
  <p class="hero-text">Corvahub highly values its strategic partnerships and is at the essence of what we are about. We have never aimed to be all things to all people and we rely on our specialist network to deliver benefits to organisations who rely on Corvahub to secure high quality talent.</p>
</header>

<nav class="site-nav">
  <div class="brand"><span class="brand-dot"></span>corvahub</div>
  <a class="nav-link" style="left:300px">HOME</a>
  <a class="nav-link" style="left:348px">HOW IT WORKS</a>
  <a class="nav-link" style="left:434px">ABOUT US</a>
  <a class="nav-link is-active" style="left:500px">OUR PARTNERS</a>
  <a class="nav-link" style="left:588px">FAQ</a>
  <a class="nav-link" style="left:627px">BLOG</a>
  <span class="account-link" style="left:771px">Log in</span>
  <span class="account-link register" style="left:801px">Register</span>
</nav>

<main>
  <h1 class="section-title">OUR PARTNERS</h1>
  <div class="title-rule"></div>

  <div class="partner-mark" style="left:238px; top:651px"><span class="mark-square"></span>Harrowgate</div>
  <h2 class="partner-name" style="left:164px; top:722px">HARROWGATE INSTITUTE OF TECHNOLOGY</h2>
  <div class="partner-rule" style="left:164px; top:744px; width:263px"></div>
  <p class="partner-copy" style="left:164px; top:757px; width:266px">Our partnership with Harrowgate is important as it enables students an alternative pathway to finding work. Starting life out as a contingent worker, arms workers with the broad experience which is vital in increasing their marketability as a respected expert.</p>

  <div class="partner-mark" style="left:530px; top:651px"><span class="mark-square"></span>Vetra</div>
  <div class="badge-shape" style="left:661px; top:638px; width:116px; height:43px"></div>
  <h2 class="partner-name" style="left:521px; top:722px; width:263px; text-align:center">VETRA</h2>
  <div class="partner-rule" style="left:521px; top:744px; width:263px"></div>
  <p class="partner-copy" style="left:521px; top:757px; width:266px">At Corvahub, we take trust very seriously. That's why we've teamed up with the Vetra Group to deliver credential verification. When searching for contractors, those with a "ASSURED" status will give you peace of mind. Companies can simply request a Vetra-powered check on a contractor through Corvahub platform. We also encourage contractors to proactively get themselves "ASSURED" to maximise their opportunities in securing quality engagements. Trust is at the centre of every successful relationship. It's especially critical in the IT workplace where consultants often have privileged access to the digital heart of your business. ASSURED powered by Vetra provides that trust. Give yourself confidence that the people you engage in your business are who they say they are, and can do the work they claim they can do. When you see the ASSURED mark associated with a candidate, you instantly know their credentials have been screened by a reputable, experienced and independent third party. Corvahub chose to partner with the Vetra Group given their unique expertise in harnessing granular local knowledge in Australia and Asia with global expertise. Its people are the architects of industry best practice; its innovative technology delivers fast and accurate results.</p>
</main>

<footer class="site-footer">
  <div class="brand"><span class="brand-dot"></span>corvahub</div>
  <p class="footer-about">Lorem Ipsum is simply dummy text of the printing and typesetting industry. Lorem Ipsum has been the industry's standard dummy</p>

  <h3 class="footer-heading" style="left:387px">SITEMAP</h3>
  <div class="footer-rule" style="left:387px; width:161px"></div>
  <ul class="footer-links" style="left:387px"><li>Home</li><li>About Us</li><li>Our Partner</li><li>FAQ</li><li>Blog</li></ul>
  <ul class="footer-links" style="left:459px"><li>Term Of Use</li><li>Privacy Policy</li><li>Contact Us</li></ul>

  <h3 class="footer-heading" style="left:626px">NEWSLETTER</h3>
  <div class="footer-rule" style="left:626px; width:161px"></div>
  <p class="newsletter-note">Subscribe to our newsletter.</p>
  <div class="email-field">Email address
    <svg class="email-arrow" width="10" height="6" viewBox="0 0 10 6"><path d="M0 3h8M6 1l2 2-2 2" stroke="#fff" stroke-width="1.2" fill="none"/></svg>
  </div>
</footer>

<div class="legal-bar">
  <span class="copyright">© Copyright 2016 Corvahub</span>
  <div class="social-links" aria-label="Social links">
    <span class="social-dot"></span><span class="social-dot"></span><span class="social-dot"></span><span class="social-dot"></span>
  </div>
</div>

</body>
</html>
```